Business Cards

I'd like help creating business cards with the full logo "Veltrona Capital Partners" on the back of the card (navy background with white writing), and abbreviated logo "VCP" on the front. Would like to list name, title, phone number, email, and website listed on front of card. Would like to keep very simple. Front font Arial or similar.

```html
<!DOCTYPE html>
<html lang="en">
<head>
<meta charset="utf-8">
<title>Veltrona Capital Partners — Business Cards</title>
<link rel="stylesheet" href="https://fonts.googleapis.com/css2?family=Arimo:wght@400;700&display=swap">
<style>
  :root {
    --backdrop: #333e44;
    --navy: #041a8c;
    --paper: #ffffff;
    --ink: #111111;
    --rule: #333333;
  }
  html, body {
    margin: 0;
    padding: 0;
    width: 1200px;
    height: 1200px;
    overflow: hidden;
    background: var(--backdrop);
    font-family: "Arimo", Arial, sans-serif;
  }
  .canvas {
    position: relative;
    width: 1200px;
    height: 1200px;
  }
  .card {
    position: absolute;
    left: 250px;
    width: 700px;
    height: 404px;
    overflow: hidden;
  }
  .card--back {
    top: 140px;
    background: var(--navy);
  }
  .card--front {
    top: 650px;
    background: var(--paper);
  }

  /* Back: full wordmark */
  .wordmark {
    position: absolute;
    left: 0;
    right: 0;
    top: 150px;
    text-align: center;
    color: var(--paper);
    font-weight: 700;
  }
  .wordmark__name {
    display: block;
    font-size: 66px;
    line-height: 66px;
    letter-spacing: 5px;
  }
  .wordmark__tagline {
    display: block;
    margin-top: 22px;
    font-size: 27px;
    line-height: 27px;
    letter-spacing: 13px;
    padding-left: 13px;
  }

  /* Front: short mark, identity, contacts */
  .shortmark {
    position: absolute;
    left: 0;
    right: 0;
    top: 100px;
    text-align: center;
    color: var(--navy);
    font-weight: 700;
    font-size: 48px;
    line-height: 48px;
    letter-spacing: 1px;
  }
  .identity {
    position: absolute;
    right: 372px;
    top: 205px;
    text-align: right;
  }
  .identity__name {
    margin: 0;
    color: var(--navy);
    font-weight: 700;
    font-size: 30px;
    line-height: 34px;
  }
  .identity__title {
    margin: 2px 0 0;
    color: var(--ink);
    font-size: 19px;
    line-height: 24px;
  }
  .divider {
    position: absolute;
    left: 349px;
    top: 193px;
    width: 1px;
    height: 81px;
    background: var(--rule);
  }
  .contacts {
    position: absolute;
    left: 385px;
    top: 195px;
    margin: 0;
    padding: 0;
    list-style: none;
  }
  .contacts__item {
    display: flex;
    align-items: center;
    height: 28px;
    color: var(--ink);
    font-size: 19px;
  }
  .contacts__icon {
    width: 14px;
    height: 14px;
    margin-right: 14px;
    flex: none;
    fill: var(--navy);
  }
  .card__band {
    position: absolute;
    left: 0;
    right: 0;
    bottom: 2px;
    height: 11px;
    background: var(--navy);
  }
</style>
</head>
<body>
<main class="canvas">
  <section class="card card--back" aria-label="Card back">
    <div class="wordmark">
      <span class="wordmark__name">VELTRONA</span>
      <span class="wordmark__tagline">CAPITAL PARTNERS</span>
    </div>
  </section>

  <section class="card card--front" aria-label="Card front">
    <div class="shortmark">VCP</div>

    <div class="identity">
      <h1 class="identity__name">DANA WHITLOCK</h1>
      <p class="identity__title">(Co-Founder)</p>
    </div>

    <div class="divider"></div>

    <ul class="contacts">
      <li class="contacts__item">
        <svg class="contacts__icon" viewBox="0 0 16 16" aria-hidden="true">
          <path d="M1 5c0-2 3-3 7-3s7 1 7 3v1.5h-3.5V5h-7v1.5H1z"/>
          <path d="M3.5 8 5 6.5h6L12.5 8v6h-9z"/>
          <circle cx="8" cy="10.5" r="1.6" fill="#fff"/>
        </svg>
        <span>1234567890</span>
      </li>
      <li class="contacts__item">
        <svg class="contacts__icon" viewBox="0 0 16 16" aria-hidden="true">
          <path d="M1 4h14v9H1z"/>
          <path d="M1.5 4.5 8 9l6.5-4.5" fill="none" stroke="#fff" stroke-width="1.4"/>
        </svg>
        <span>veltronacp@mail.com</span>
      </li>
      <li class="contacts__item">
        <svg class="contacts__icon" viewBox="0 0 16 16" aria-hidden="true">
          <circle cx="8" cy="8" r="7"/>
          <path d="M5 4.5c1.5 0 2 1 1.5 2S4.5 8 5.5 9.5 6 12 7 12.5M10.5 3.5c-.5 1 0 2 1.2 2.3M12.5 10c-1 0-2 .5-2 1.8" fill="none" stroke="#fff" stroke-width="1.2"/>
        </svg>
        <span>www.veltronacp.com</span>
      </li>
    </ul>

    <div class="card__band"></div>
  </section>
</main>
</body>
</html>
```